Kestrel Roofing & Restoration Business Card Design

Lookiing for a double sided business card design that will have rounded corners, will look good with Spot UV, Soft Laminate, or Gloss
Front of card should have Logo, Name and Contact Info, License numbers
Back of card should have Logo, maybe other small details

```html
<!DOCTYPE html>
<html lang="en">
<head>
<meta charset="UTF-8">
<title>Kestrel Roofing &amp; Restoration — Business Card</title>
<link href="https://fonts.googleapis.com/css2?family=Poppins:wght@300;400;500;700&display=swap" rel="stylesheet">
<style>
  :root {
    --stage: #2b2b2d;
    --card: #0d0d0e;
    --edge: #1aa3e0;
    --accent: #1aa3e0;
    --ink: #ffffff;
    --ink-soft: #c9c9cc;
    --rule: #4a4a4d;
  }
  * { margin: 0; padding: 0; box-sizing: border-box; }
  html, body { width: 1200px; height: 900px; overflow: hidden; }
  body {
    background: var(--stage);
    font-family: "Poppins", sans-serif;
    display: flex;
    flex-direction: column;
    align-items: center;
    justify-content: center;
    gap: 56px;
  }
  .card {
    position: relative;
    width: 620px;
    height: 354px;
    background: var(--card);
    border-radius: 22px;
    border-bottom: 6px solid var(--edge);
    overflow: hidden;
  }
  .brand {
    position: absolute;
    display: flex;
    align-items: center;
    gap: 12px;
    color: var(--ink);
    font-weight: 700;
    text-transform: uppercase;
    letter-spacing: 0.5px;
  }
  .brand__mark {
    width: 16px; height: 16px;
    background: var(--accent);
    flex: none;
  }
  .brand__name { line-height: 1.15; }

  .card--front .brand { left: 40px; top: 200px; font-size: 17px; }
  .card--front .divider {
    position: absolute;
    left: 300px; top: 44px;
    width: 1px; height: 250px;
    background: var(--rule);
  }
  .contact {
    position: absolute;
    left: 328px; top: 52px;
    color: var(--ink-soft);
  }
  .contact__name {
    color: var(--accent);
    font-weight: 700;
    font-size: 22px;
    line-height: 1.1;
    text-transform: uppercase;
  }
  .contact__title { font-size: 13px; font-weight: 400; margin-top: 2px; }
  .contact__license {
    font-size: 12px; color: var(--accent); text-transform: uppercase; margin-top: 2px;
  }
  .contact__license span { color: var(--ink); }
  .contact__list { list-style: none; margin-top: 16px; font-size: 13px; font-weight: 300; }
  .contact__list li { display: flex; align-items: center; gap: 8px; line-height: 1.7; }
  .contact__list svg { width: 13px; height: 13px; flex: none; }
  .contact__address { margin-top: 14px; font-size: 13px; font-weight: 300; line-height: 1.5; }

  .card--back .brand {
    left: 50%; top: 50%;
    transform: translate(-50%, -50%);
    font-size: 26px;
    color: var(--ink-soft);
  }
  .card--back .brand__mark { width: 22px; height: 22px; background: var(--ink-soft); }
</style>
</head>
<body>

  <section class="card card--front" aria-label="Card front">
    <div class="brand">
      <span class="brand__mark"></span>
      <span class="brand__name">Kestrel Roofing<br>&amp; Restoration</span>
    </div>
    <div class="divider"></div>
    <div class="contact">
      <h1 class="contact__name">Marcus Hale</h1>
      <p class="contact__title">Managing Director</p>
      <p class="contact__license">License number: <span>XXXXX</span></p>
      <ul class="contact__list">
        <li>
          <svg viewBox="0 0 24 24" fill="var(--accent)"><path d="M6.6 10.8a15 15 0 0 0 6.6 6.6l2.2-2.2a1 1 0 0 1 1-.25 11.4 11.4 0 0 0 3.6.57 1 1 0 0 1 1 1V20a1 1 0 0 1-1 1A17 17 0 0 1 3 4a1 1 0 0 1 1-1h3.5a1 1 0 0 1 1 1c0 1.25.2 2.450.57 3.6a1 1 0 0 1-.25 1z"/></svg>
          044-987 654 321
        </li>
        <li>
          <svg viewBox="0 0 24 24" fill="var(--accent)"><path d="M2 5h20v14H2z M2 5l10 8 10-8" stroke="var(--card)" stroke-width="1.6"/></svg>
          hello@kestrelroof.com
        </li>
        <li>
          <svg viewBox="0 0 24 24" fill="none" stroke="var(--accent)" stroke-width="2"><circle cx="12" cy="12" r="10"/><path d="M2 12h20M12 2a15 15 0 0 1 0 20M12 2a15 15 0 0 0 0 20"/></svg>
          www.kestrelroof.com
        </li>
      </ul>
      <p class="contact__address">18, Harbour View Road<br>30718, Country Name</p>
    </div>
  </section>

  <section class="card card--back" aria-label="Card back">
    <div class="brand">
      <span class="brand__mark"></span>
      <span class="brand__name">Kestrel Roofing<br>&amp; Restoration</span>
    </div>
  </section>

</body>
</html>
```